Varnok - Business Card Design

Design a modern masculine business card for our business

Target Market(s)

Private Market

Industry/Entity Type

Construction

Contact Information for Business Card

Company Name - Name of Person - Address - email address - contact number

Font styles to use
Serif
Sans Serif

Colors
0094D4
00A9DD
6FCCEA
C7EBF8
E9F6FB
00AB8E
00BBA5
67D7C9
C6EFE9
E9F9F6
F0912C
F2A743
F7CA91
FBE8D2
FDF5EE

Requirements
Must have
• Use company logo provided
Nice to have
• Company Logo

```html
<!DOCTYPE html>
<html lang="en">
<head>
<meta charset="utf-8">
<title>Varnok Construction – Business Card</title>
<link rel="stylesheet" href="https://fonts.googleapis.com/css2?family=Montserrat:wght@400;600;700&family=Bebas+Neue&display=swap">
<style>
  :root {
    --backdrop: #b3b3b3;
    --card-light: #ffffff;
    --card-dark: #000000;
    --ink: #111111;
    --accent: #f37130;
    --on-dark: #ffffff;
  }
  * { margin: 0; padding: 0; box-sizing: border-box; }
  html, body {
    width: 1000px;
    height: 1200px;
    overflow: hidden;
    background: var(--backdrop);
    font-family: "Montserrat", sans-serif;
  }
  .canvas {
    position: relative;
    width: 1000px;
    height: 1200px;
  }
  .card {
    position: absolute;
    left: 51px;
    width: 898px;
    height: 539px;
  }
  .card--front { top: 44px; background: var(--card-light); }
  .card--back  { top: 616px; background: var(--card-dark); }

  .brand {
    position: absolute;
    display: flex;
    align-items: center;
    font-family: "Montserrat", sans-serif;
    font-weight: 700;
    letter-spacing: 0.01em;
    line-height: 1;
    white-space: nowrap;
  }
  .brand__mark {
    display: block;
    flex: none;
    background: var(--accent);
  }
  .card--front .brand {
    left: 57px;
    top: 66px;
    gap: 16px;
    font-size: 84px;
    color: var(--ink);
  }
  .card--front .brand__mark { width: 56px; height: 56px; }
  .card--back .brand {
    left: 194px;
    top: 212px;
    gap: 20px;
    font-size: 96px;
    color: var(--on-dark);
  }
  .card--back .brand__mark { width: 66px; height: 66px; }

  .contact {
    position: absolute;
    left: 552px;
    top: 254px;
    color: var(--ink);
  }
  .contact__name {
    font-size: 25px;
    font-weight: 600;
    line-height: 1.2;
  }
  .contact__role {
    font-size: 25px;
    font-weight: 400;
    line-height: 1.3;
    margin-bottom: 12px;
  }
  .contact__list { list-style: none; }
  .contact__item {
    display: flex;
    align-items: center;
    gap: 9px;
    height: 40px;
    font-size: 24px;
    font-weight: 400;
    white-space: nowrap;
  }
  .contact__icon {
    flex: none;
    width: 26px;
    height: 26px;
    background: var(--accent);
    border-radius: 2px;
  }

  .tagline {
    position: absolute;
    left: 0;
    right: 0;
    top: 455px;
    text-align: center;
    font-family: "Bebas Neue", sans-serif;
    font-size: 44px;
    letter-spacing: 0.02em;
    color: var(--on-dark);
    white-space: nowrap;
  }
</style>
</head>
<body>
<main class="canvas">

  <section class="card card--front" aria-label="Business card front">
    <div class="brand"><span class="brand__mark"></span>VARNOK</div>

    <div class="contact">
      <p class="contact__name">Your Name</p>
      <p class="contact__role">Manager</p>
      <ul class="contact__list">
        <li class="contact__item">
          <svg class="contact__icon" viewBox="0 0 26 26" aria-hidden="true">
            <path d="M9 6.5l2.3 3-1.4 1.6c.9 2 2.2 3.4 4 4.4l1.6-1.4 3 2.3-1.4 2.4c-4.6-.4-9-4.9-9.4-9.8z" fill="#fff"/>
          </svg>
          123 444 555
        </li>
        <li class="contact__item">
          <svg class="contact__icon" viewBox="0 0 26 26" aria-hidden="true">
            <path d="M13 5.5a5 5 0 0 0-5 5c0 3.6 5 9 5 9s5-5.4 5-9a5 5 0 0 0-5-5z" fill="none" stroke="#fff" stroke-width="1.6"/>
            <circle cx="13" cy="10.5" r="1.8" fill="#fff"/>
            <line x1="9" y1="21" x2="17" y2="21" stroke="#fff" stroke-width="1.4"/>
          </svg>
          789 Your Street Here
        </li>
        <li class="contact__item">
          <svg class="contact__icon" viewBox="0 0 26 26" aria-hidden="true">
            <rect x="5.5" y="8" width="15" height="10.5" fill="none" stroke="#fff" stroke-width="1.5"/>
            <path d="M5.5 8l7.5 6 7.5-6M5.5 18.5l5.5-5M20.5 18.5l-5.5-5" fill="none" stroke="#fff" stroke-width="1.3"/>
          </svg>
          info@yourname.com
        </li>
        <li class="contact__item">
          <svg class="contact__icon" viewBox="0 0 26 26" aria-hidden="true">
            <circle cx="13" cy="13" r="7" fill="none" stroke="#fff" stroke-width="1.5"/>
            <ellipse cx="13" cy="13" rx="3" ry="7" fill="none" stroke="#fff" stroke-width="1.3"/>
            <path d="M6 13h14M7 9.5h12M7 16.5h12" stroke="#fff" stroke-width="1.2"/>
          </svg>
          www.yourname.com
        </li>
      </ul>
    </div>
  </section>

  <section class="card card--back" aria-label="Business card back">
    <div class="brand"><span class="brand__mark"></span>VARNOK</div>
    <p class="tagline">Construction, Inc is more taller and noticable here</p>
  </section>

</main>
</body>
</html>
```